Business Card Design

We are a manufacturing company that has been in business for over 30 years, established in 1981. We are looking to increase our business with defence force, government, and the major telecoms so the card needs to present the company as being cutting edge, secure, and professional.
Industry/Entity Type
Defence
Contact Information for Business Card
Name Gareth Olsund
Phone 02 9374 6815
Fax 02 9457 3162
mobile 0438260517
Email Gary@Korvex.com.au
Webiste www.korvex.com.au
ABN 58 006 391 842
address: 17 Belcor Street Ingleburn NSW 2565
"Makers of Antenna Arrays, GNSS, Radar, Cable Harnesses, RF, Defence, & Telecom Systems"
Look and feel

```html
<!DOCTYPE html>
<html lang="en">
<head>
<meta charset="UTF-8">
<title>Korvex Business Card</title>
<link rel="stylesheet" href="https://fonts.googleapis.com/css2?family=Oswald:wght@500;600&family=Roboto:wght@400;500;700&display=swap">
<style>
  :root {
    --navy: #1f2557;
    --red: #c2452d;
    --white: #ffffff;
    --ink: #1f2557;
    --backdrop: #ececec;
  }
  * { box-sizing: border-box; margin: 0; padding: 0; }
  html, body {
    width: 1200px;
    height: 695px;
    overflow: hidden;
    background: var(--backdrop);
    font-family: "Roboto", Arial, sans-serif;
    color: var(--ink);
  }
  .canvas {
    position: relative;
    width: 1200px;
    height: 695px;
  }
  .card {
    position: absolute;
    top: 187px;
    width: 560px;
    height: 320px;
    background: var(--navy);
    overflow: hidden;
    box-shadow: 0 6px 18px rgba(0, 0, 0, 0.18);
  }
  .card--front { left: 20px; }
  .card--back { left: 620px; }
  .card__shape {
    position: absolute;
    inset: 0;
    width: 100%;
    height: 100%;
  }
  .shape-red { fill: var(--red); }
  .shape-white { fill: var(--white); }

  /* Contact side */
  .contact {
    position: absolute;
    left: 22px;
    top: 44px;
    width: 380px;
  }
  .contact__address {
    display: flex;
    align-items: flex-start;
    gap: 9px;
    font-size: 14px;
    font-weight: 500;
    line-height: 18px;
  }
  .contact__rows {
    margin-top: 24px;
    display: grid;
    grid-template-columns: 128px 118px 130px;
    row-gap: 16px;
    font-size: 14px;
    font-weight: 500;
  }
  .contact__item {
    display: flex;
    align-items: center;
    gap: 8px;
    white-space: nowrap;
  }
  .contact__item--wide { grid-column: span 2; }
  .icon {
    flex: 0 0 auto;
    width: 22px;
    height: 22px;
    border-radius: 4px;
    background: var(--red);
    display: flex;
    align-items: center;
    justify-content: center;
  }
  .icon svg { width: 14px; height: 14px; fill: var(--white); }
  .icon--pin { background: none; }
  .icon--pin svg { width: 20px; height: 24px; fill: var(--red); }
  .icon--abn {
    font-size: 9px;
    font-weight: 700;
    color: var(--white);
    width: 24px;
  }
  .holder-name {
    position: absolute;
    left: 495px;
    top: 160px;
    transform: translate(-50%, -50%) rotate(-90deg);
    font-family: "Oswald", "Arial Narrow", sans-serif;
    font-weight: 600;
    font-size: 32px;
    letter-spacing: 1px;
    color: var(--white);
    text-transform: uppercase;
    white-space: nowrap;
  }

  /* Brand side */
  .brand {
    position: absolute;
    left: 100px;
    top: 70px;
    width: 190px;
    display: flex;
    flex-direction: column;
    align-items: center;
  }
  .brand__mark {
    width: 84px;
    height: 84px;
    background: var(--navy);
  }
  .brand__name {
    margin-top: 10px;
    font-family: "Roboto", Arial, sans-serif;
    font-weight: 700;
    font-size: 24px;
    letter-spacing: 2px;
    color: var(--red);
  }
  .brand__web {
    margin-top: 20px;
    font-size: 14px;
    font-weight: 500;
    color: var(--ink);
  }
</style>
</head>
<body>
<main class="canvas">

  <section class="card card--front" aria-label="Business card, contact side">
    <svg class="card__shape" viewBox="0 0 560 320" aria-hidden="true">
      <path class="shape-red" d="M0 0 H354 C436 50 464 205 390 320 H0 Z"/>
      <path class="shape-white" d="M0 0 H322 C420 42 456 205 362 320 H0 Z"/>
    </svg>

    <div class="contact">
      <div class="contact__address">
        <span class="icon icon--pin">
          <svg viewBox="0 0 20 24"><path d="M10 0C4.5 0 0 4.3 0 9.6 0 16.8 10 24 10 24s10-7.2 10-14.4C20 4.3 15.5 0 10 0zm0 13.5a4 4 0 1 1 0-8 4 4 0 0 1 0 8z"/></svg>
        </span>
        <p>17 Belcor Street Marlden NSW 2743”<br>Makers of Antenna Arrays, GNSS, Radar,<br>Cable Harnesses, RF, Defence, &amp;<br>Telecom Systems”</p>
      </div>

      <div class="contact__rows">
        <div class="contact__item">
          <span class="icon"><svg viewBox="0 0 24 24"><path d="M6.6 10.8a15.1 15.1 0 0 0 6.6 6.6l2.2-2.2c.3-.3.7-.4 1-.2 1.1.4 2.3.6 3.6.6.6 0 1 .4 1 1V20c0 .6-.4 1-1 1A17 17 0 0 1 3 4c0-.6.4-1 1-1h3.5c.6 0 1 .4 1 1 0 1.3.2 2.5.6 3.6.1.3 0 .7-.2 1z"/></svg></span>
          02 9374 6815
        </div>
        <div class="contact__item">
          <span class="icon"><svg viewBox="0 0 24 24"><path d="M7 1h10a2 2 0 0 1 2 2v18a2 2 0 0 1-2 2H7a2 2 0 0 1-2-2V3a2 2 0 0 1 2-2zm0 3v14h10V4zm5 15.5a1.2 1.2 0 1 0 0 2.4 1.2 1.2 0 0 0 0-2.4z"/></svg></span>
          0438260517
        </div>
        <div class="contact__item">
          <span class="icon"><svg viewBox="0 0 24 24"><path d="M6 2h9l3 3v4h1a3 3 0 0 1 3 3v7h-4v3H6v-3H2v-7a3 3 0 0 1 3-3h1zm2 2v5h8V6h-2V4zm0 11v5h8v-5z"/></svg></span>
          02 9457 3162
        </div>
        <div class="contact__item contact__item--wide">
          <span class="icon"><svg viewBox="0 0 24 24"><path d="M2 5h20v14H2zm2 2v.5l8 5.5 8-5.5V7zm0 3v7h16v-7l-8 5.5z"/></svg></span>
          Gary@Korvex.com.au
        </div>
        <div class="contact__item">
          <span class="icon icon--abn">Abn</span>
          58 006 391 842
        </div>
      </div>
    </div>

    <h1 class="holder-name">Gareth Olsund</h1>
  </section>

  <section class="card card--back" aria-label="Business card, brand side">
    <svg class="card__shape" viewBox="0 0 560 320" aria-hidden="true">
      <path class="shape-red" d="M0 0 H356 C448 60 458 240 396 320 H0 Z"/>
      <path class="shape-white" d="M0 0 H330 C430 60 442 245 372 320 H0 Z"/>
    </svg>

    <div class="brand">
      <div class="brand__mark" aria-hidden="true"></div>
      <p class="brand__name">KORVEX</p>
      <p class="brand__web">www.korvex.com.au</p>
    </div>
  </section>

</main>
</body>
</html>
```